New Business Card Design for Manufacturing

We are an engineering/manufacturing company that offers Advanced machining/assembly/engineering services, as well as innovative products for the heavy duty engine cooling markets.

We are looking to get a new business card designed that is clean and modern looking, but still fits the wide range of technical/skilled work we do.

- We hope to use this design as the base for other design work in new Presentations, web, and print work.

Industry/Entity Type

Engineering

Contact Information for Business Card

Our preferred color of blue is (RGB) 22/71/159 but can vary slightly from that color. Our content will be our Logo and full company name (Fabricated Tooling Works, Inc.), company address, name, job title, phone number with extension, cell number, fax number, website, and email address on the cards.
We'd like the full company name next to the logo, but we are open to other interpretations of that layout.
Preferably, we would like the back side to be clean with just our logo, and the front to contain all of the contact information.

Colors
2f74b4
0355a3
85abd2

Requirements
Must have
• - Logo, company name, needed content - We are open to interpretation beyond that.
• - Standard size business card.
• - Horizontal orientation.
• - Enough space for lengthy names / job titles (for example, a job title could read "Directory of Human Resources" or "V.P. of Governmental Affairs"). We need this to look clean, whether the title be short (CEO) or long (as described above).

```html
<!DOCTYPE html>
<html lang="en">
<head>
<meta charset="utf-8">
<title>Fabricated Tooling Works – Business Card</title>
<link rel="stylesheet" href="https://fonts.googleapis.com/css2?family=Open+Sans:wght@400;700&display=swap">
<style>
  :root {
    --backdrop: #dcdcdc;
    --brand-blue: #0b5196;
    --card-white: #ffffff;
    --text-light: #ffffff;
    --rule-light: rgba(255, 255, 255, 0.85);
  }
  * { margin: 0; padding: 0; box-sizing: border-box; }
  html, body {
    width: 1200px;
    height: 576px;
    overflow: hidden;
    background: var(--backdrop);
    font-family: "Open Sans", Arial, sans-serif;
  }
  .canvas {
    position: relative;
    width: 1200px;
    height: 576px;
  }
  .card {
    position: absolute;
    top: 138px;
    width: 483px;
    height: 294px;
    border-radius: 16px;
    overflow: hidden;
  }

  /* Back side */
  .card-back {
    left: 81px;
    background: var(--brand-blue);
  }
  .card-back .brand-name {
    position: absolute;
    left: 0;
    right: 0;
    top: 112px;
    text-align: center;
    color: var(--text-light);
    font-weight: 700;
    font-size: 30px;
    line-height: 40px;
  }
  .card-back .website-row {
    position: absolute;
    left: 0;
    right: 0;
    top: 264px;
    display: flex;
    justify-content: center;
    align-items: center;
    gap: 10px;
    color: var(--text-light);
    font-size: 13px;
    line-height: 18px;
  }
  .website-row .rule {
    width: 52px;
    height: 2px;
    background: var(--rule-light);
    border-radius: 1px;
  }

  /* Front side */
  .card-front {
    left: 602px;
    background: var(--card-white);
  }
  .card-front .curve-band {
    position: absolute;
    inset: 0;
    width: 483px;
    height: 294px;
  }
  .card-front .curve-band path { fill: var(--brand-blue); }
  .card-front .brand-name {
    position: absolute;
    left: 0;
    right: 0;
    top: 44px;
    text-align: center;
    color: var(--brand-blue);
    font-weight: 700;
    font-size: 25px;
    line-height: 34px;
  }
  .person {
    position: absolute;
    right: 26px;
    top: 158px;
    text-align: right;
    color: var(--text-light);
  }
  .person-name {
    font-size: 20px;
    line-height: 26px;
  }
  .person-title {
    font-size: 12px;
    line-height: 16px;
  }
  .address {
    position: absolute;
    right: 26px;
    top: 219px;
    text-align: right;
    color: var(--text-light);
    font-size: 13px;
    line-height: 17.3px;
  }
  .contact-list {
    position: absolute;
    left: 25px;
    top: 202px;
    list-style: none;
    color: var(--text-light);
    font-size: 13px;
    line-height: 17.3px;
  }
  .contact-list li {
    display: flex;
    align-items: center;
    gap: 9px;
  }
  .contact-list svg {
    width: 11px;
    height: 11px;
    fill: var(--text-light);
    flex: none;
  }
</style>
</head>
<body>
<main class="canvas">

  <section class="card card-back" aria-label="Card back">
    <div class="brand-name">Fabricated Tooling Works</div>
    <div class="website-row">
      <span class="rule"></span>
      <span>www.yourwebsite.com</span>
      <span class="rule"></span>
    </div>
  </section>

  <section class="card card-front" aria-label="Card front">
    <svg class="curve-band" viewBox="0 0 483 294" preserveAspectRatio="none" aria-hidden="true">
      <path d="M0 84 Q241.5 172 483 84 L483 294 L0 294 Z"/>
    </svg>
    <div class="brand-name">Fabricated Tooling Works</div>

    <div class="person">
      <div class="person-name">John Doe Smith</div>
      <div class="person-title">Managing Director</div>
    </div>

    <ul class="contact-list">
      <li>
        <svg viewBox="0 0 12 12" aria-hidden="true"><path d="M1 4 Q6 0 11 4 L10 5.5 L8 4.5 L8 3.5 Q6 2.8 4 3.5 L4 4.5 L2 5.5 Z M3 6 H9 L10 11 H2 Z"/></svg>
        <span>111-2222-2222 (FTW)</span>
      </li>
      <li>
        <svg viewBox="0 0 12 12" aria-hidden="true"><path d="M3 0.5 H9 Q10 0.5 10 1.5 V10.5 Q10 11.5 9 11.5 H3 Q2 11.5 2 10.5 V1.5 Q2 0.5 3 0.5 Z M3.3 2 V8.5 H8.7 V2 Z"/></svg>
        <span>333-3333-3333</span>
      </li>
      <li>
        <svg viewBox="0 0 12 12" aria-hidden="true"><path d="M3 0.5 H9 V4 H3 Z M1 4.5 H11 V9 H9 V11.5 H3 V9 H1 Z M4 8 V10.5 H8 V8 Z"/></svg>
        <span>444-4444-4444</span>
      </li>
      <li>
        <svg viewBox="0 0 12 12" aria-hidden="true"><path d="M0.5 2.5 H11.5 V9.5 H0.5 Z M1.5 3.3 L6 6.6 L10.5 3.3 Z" fill-rule="evenodd"/></svg>
        <span>johndoe@yourwebsite.com</span>
      </li>
    </ul>

    <div class="address">
      <div>234 Anywhere St., Any City,</div>
      <div>Any Town, US 123456</div>
      <div>www.yourwebsite.com</div>
    </div>
  </section>

</main>
</body>
</html>
```